Career Counselor in need of a business card design

Hello Creatives! I'm in need of a business card design for a new company based in Georgia, USA called Pathways By Lantern.

Some things that may be helpful in creating your concept(s) include:

My Logo (Included in the Files section): There are three versions, two versions are in the second file. The all gold stacked (vertical) version is my primary logo and then there are two horizontal versions (one is all gold and the other is gold and grey).

My mission: to empower tweens through young adults to realize and actualize their CAREER ASPIRATIONS.
My vision: for tweens through young adults to LIVE LIFE ON PURPOSE and become CONTRIBUTING MEMBERS OF SOCIETY.

Biblical scriptures that support my ‘Why’: Psalms 127: 3-4(NIV) Children are a heritage from the Lord, offspring a reward from him. Like ARROWS in the hands of a warrior are children…. And Proverbs 29:18(JKV) Where there is no VISION, the people perish.

*Words in ALL CAPS are to emphasize what's important to me and may possibly provide you some inspiration (IDK - Have fun with it)!

Target Market(s)

My ideal customers are parents, guardians, and young adults.

Contact Information for Business Card

My name, degrees and credential: Delphine Marlow, M.S., Ed.S., NCC
Title: College and Career Coach and Consultant

Number: 555.318.2907
Address: 2718 Willowmere Avenue., Suite 405, Macon, GA 31299
Email: info@pathwaysbylantern.example
Website: www.pathwaysbylantern.example

My population: TWEENS • TEENS • EMERGING ADULTS
Services offered: One-On-One Sessions • Small Groups • Workshops

Colors

Designer to choose colors to be used in the design.

Requirements
Nice to have
• Either my mission or vision but I will understand if it does not all fit.
• My mission: To empower tweens through young adults to realize and actualize their career aspirations.
• My vision: For tweens through young adults to live life on purpose and become contributing members of society.

```html
<!DOCTYPE html>
<html lang="en">
<head>
<meta charset="utf-8">
<title>Pathways By Lantern – Business Card</title>
<link href="https://fonts.googleapis.com/css2?family=Cinzel:wght@400;600;700&display=swap" rel="stylesheet">
<style>
  :root {
    --backdrop: #86cfb0;
    --ink: #0b0b0b;
    --gold: #d9b24a;
    --gold-band: #e0b84f;
    --paper: #ffffff;
    --text-dark: #141414;
  }
  * { margin: 0; padding: 0; box-sizing: border-box; }
  html, body {
    width: 1200px; height: 1000px; overflow: hidden;
    background: var(--backdrop);
    font-family: "Cinzel", "Times New Roman", serif;
  }
  .canvas { position: relative; width: 1200px; height: 1000px; }

  /* Front of card */
  .card-front {
    position: absolute; left: 297px; top: 112px;
    width: 605px; height: 345px;
    background: var(--ink);
    display: flex; flex-direction: column; align-items: center; justify-content: center;
    gap: 14px;
  }
  .brand-mark { display: block; }
  .brand-name {
    color: var(--gold);
    font-weight: 600;
    font-size: 46px;
    line-height: 1.05;
    text-align: center;
    letter-spacing: 1px;
  }

  /* Back of card */
  .card-back {
    position: absolute; left: 297px; top: 515px;
    width: 608px; height: 347px;
    background: var(--paper);
  }
  .name-band {
    position: absolute; left: 0; top: 0; width: 100%; height: 135px;
    background: var(--gold-band);
    text-align: center;
    color: var(--text-dark);
  }
  .name-band::after {
    content: ""; position: absolute; left: 289px; top: 135px;
    border-left: 15px solid transparent; border-right: 15px solid transparent;
    border-top: 15px solid var(--gold-band);
  }
  .person-name {
    position: absolute; left: 0; right: 0; top: 40px;
    font-size: 25px; font-weight: 700; letter-spacing: 0.5px;
  }
  .person-title {
    position: absolute; left: 0; right: 0; top: 75px;
    font-size: 17.5px; font-weight: 700;
  }
  .contact {
    position: absolute; left: 33px; top: 166px; width: 262px;
    font-size: 14.5px; font-weight: 400; color: var(--text-dark);
  }
  .address { line-height: 18px; white-space: nowrap; }
  .contact-list { list-style: none; margin-top: 20px; }
  .contact-list li {
    display: flex; align-items: center; gap: 8px;
    height: 20px; line-height: 20px;
    white-space: nowrap;
  }
  .contact-list .phone { font-size: 14.5px; }
  .contact-list .web { font-size: 12px; letter-spacing: -0.1px; }
  .contact-list svg { flex: none; }
  .divider {
    position: absolute; left: 303px; top: 162px;
    width: 2px; height: 120px; background: var(--text-dark);
  }
  .mission {
    position: absolute; right: 35px; top: 163px;
    text-align: right; white-space: nowrap;
    font-size: 14.5px; font-weight: 400; line-height: 31.5px; color: var(--text-dark);
  }
  .services-band {
    position: absolute; left: 0; bottom: 0; width: 100%; height: 50px;
    background: var(--ink);
    color: var(--gold);
    font-size: 16.5px; font-weight: 400; letter-spacing: 0.3px;
    display: flex; align-items: center; justify-content: center;
  }
</style>
</head>
<body>
<div class="canvas">

  <section class="card-front">
    <svg class="brand-mark" width="90" height="90" viewBox="0 0 90 90" aria-hidden="true">
      <circle cx="45" cy="45" r="41" fill="none" stroke="#d9b24a" stroke-width="4"/>
    </svg>
    <h1 class="brand-name">Pathways<br>By Lantern</h1>
  </section>

  <section class="card-back">
    <header class="name-band">
      <h2 class="person-name">Delphine Marlow, M.S., Ed.S., NCC</h2>
      <p class="person-title">College and Career Counselor and Consultant</p>
    </header>

    <div class="contact">
      <p class="address">2718 Willowmere Avenue<br>Suite 405, Macon, GA 31299</p>
      <ul class="contact-list">
        <li class="phone">
          <svg width="16" height="12" viewBox="0 0 16 12" aria-hidden="true">
            <path d="M1 4 Q8 -1 15 4 L13 6 L11 4 L5 4 L3 6 Z" fill="#d9b24a"/>
            <rect x="4" y="6" width="8" height="5" rx="1" fill="#d9b24a"/>
          </svg>
          <span>555.318.2907</span>
        </li>
        <li class="web">
          <svg width="16" height="12" viewBox="0 0 16 12" aria-hidden="true">
            <rect x="1" y="1" width="14" height="10" fill="none" stroke="#d9b24a" stroke-width="1.5"/>
            <path d="M1 1 L8 7 L15 1" fill="none" stroke="#d9b24a" stroke-width="1.5"/>
          </svg>
          <span>info@pathwaysbylantern.example</span>
        </li>
        <li class="web">
          <svg width="16" height="14" viewBox="0 0 16 16" aria-hidden="true">
            <circle cx="8" cy="8" r="6.5" fill="none" stroke="#d9b24a" stroke-width="1.5"/>
            <ellipse cx="8" cy="8" rx="3" ry="6.5" fill="none" stroke="#d9b24a" stroke-width="1.2"/>
            <line x1="1.5" y1="8" x2="14.5" y2="8" stroke="#d9b24a" stroke-width="1.2"/>
          </svg>
          <span>www.pathwaysbylantern.example</span>
        </li>
      </ul>
    </div>

    <div class="divider"></div>

    <p class="mission">Empowering tweens<br>through young adults to<br>realize and actualize their<br>career aspirations.</p>

    <footer class="services-band">One-On-One Sessions · Small Groups · Workshops</footer>
  </section>

</div>
</body>
</html>
```